Brightmoor Cleaning Services

need a brochure for my cleaning company. Contact info coming soon .

Target Market(s)

Cleaning Services

Industry/Entity Type

Cleaning Service

Requirements
Must have
• I attached logo for you to use.

Corporate address -
472 Kestrel Ridge W Ste 518
Tukwila, WA 98102

Phone number - 877-514-SHINE
Nice to have
• bifold brochure. I attached some samples
Should not have
• Pictures of people. Keep it clean and professional.

```html
<!DOCTYPE html>
<html lang="en">
<head>
<meta charset="utf-8">
<title>Brightmoor Cleaning Services – Bifold Brochure</title>
<link href="https://fonts.googleapis.com/css2?family=Lato:ital,wght@0,400;0,700;1,400&family=Oswald:wght@600&display=swap" rel="stylesheet">
<style>
  :root{
    --red:#e31e26;
    --blue:#1a6dbf;
    --blue-deep:#1560b0;
    --ink:#222;
    --paper:#fff;
    --stage:#333;
    --photo-light:#dfe3e8;
    --photo-warm:#d9d2c6;
  }
  *{box-sizing:border-box;margin:0;padding:0}
  html,body{width:840px;height:1200px;overflow:hidden}
  body{background:var(--stage);font-family:'Lato',sans-serif;color:var(--ink);position:relative}
  .spread{position:absolute;left:20px;width:800px;height:566px;display:flex;background:var(--paper);box-shadow:0 6px 18px rgba(0,0,0,.45)}
  .spread--outside{top:20px}
  .spread--inside{top:614px}
  .page{position:relative;width:400px;height:566px;overflow:hidden}
  .page + .page{border-left:1px solid #e6e6e6}
  .photo{position:absolute}

  /* back cover */
  .back__photo{left:0;top:0;width:400px;height:420px;background:linear-gradient(160deg,#eef1f4 0%,#c9d3de 45%,#3f6fa8 70%,#dfe3e8 100%)}
  .brand{display:flex;align-items:center;gap:6px;color:var(--blue);font-family:'Lato',sans-serif;font-weight:700;line-height:1.15}
  .brand__dot{width:14px;height:14px;border-radius:50%;background:var(--red);flex:none}
  .back__brand{position:absolute;left:24px;top:448px;width:120px;font-size:14px}
  .contact{position:absolute;left:170px;top:440px;font-size:9.5px;line-height:1.35}
  .contact__row{display:flex;align-items:flex-start;gap:8px;margin-bottom:7px}
  .contact__row svg{flex:none;margin-top:1px}
  .contact__phone{font-weight:700;font-size:12px}

  /* front cover */
  .front__band{position:absolute;left:0;top:0;width:400px;height:96px;background:var(--red);display:flex;align-items:center;justify-content:center;text-align:center}
  .front__headline{font-family:'Oswald',sans-serif;font-weight:600;color:#fff;font-size:23px;line-height:1.1;text-transform:uppercase;letter-spacing:.3px}
  .front__photo{left:0;top:96px;width:400px;height:380px;background:linear-gradient(135deg,#f1f1ef 0%,#dcdcd8 50%,#c9c7bd 80%,#e8d36a 100%)}
  .testimonials{position:absolute;left:22px;top:300px;width:216px;height:222px;background:var(--blue);color:#fff;padding:22px 12px 10px;border-top:8px solid var(--red)}
  .testimonials__title{font-size:14px;letter-spacing:.5px;display:flex;align-items:center;gap:8px;margin-top:-12px;margin-bottom:8px;border-bottom:1px solid rgba(255,255,255,.5);padding-bottom:5px}
  .review{margin-bottom:9px}
  .review__head{font-weight:700;font-size:9px}
  .review__by{font-size:8px}
  .review__stars{color:#f5c518;font-size:7px;letter-spacing:1px}
  .review__text{font-size:6.5px;line-height:1.35}
  .front__url{position:absolute;left:22px;top:530px;color:var(--red);font-size:12px;letter-spacing:5px}
  .front__brand{position:absolute;left:262px;top:488px;width:120px;font-size:14px}

  /* inside left */
  .inside-left{padding:22px 24px}
  .words__title{font-size:12px;font-style:italic;margin-bottom:5px}
  .body-text{font-size:7px;line-height:1.4}
  .quote-block{position:absolute;left:0;top:118px;width:400px;height:160px}
  .quote-box{position:absolute;left:110px;top:14px;width:276px;height:140px;background:var(--red);color:#fff;padding:18px 18px 10px 82px;font-size:7px;line-height:1.4;border-radius:0 0 0 0}
  .quote-box__mark{position:absolute;font-family:'Oswald',sans-serif;font-size:30px;line-height:1}
  .quote-box__mark--open{left:60px;top:6px}
  .quote-box__mark--close{right:10px;bottom:-6px}
  .quote-box__by{margin-top:4px;letter-spacing:2px}
  .quote-photo{position:absolute;left:22px;top:0;width:148px;height:148px;border-radius:50%;background:radial-gradient(circle at 50% 40%,#f3efe8 0%,#a9c6da 55%,#3a78b5 100%);border:3px solid #fff}
  .section-title{color:var(--blue);font-weight:400}
  .carpet{position:absolute;left:24px;top:298px;width:352px}
  .carpet .section-title{font-size:15px;border-bottom:2px solid var(--blue);padding-bottom:3px;margin-bottom:5px;display:inline-block}
  .reasons{position:absolute;left:24px;top:378px;width:352px}
  .reasons .section-title{font-size:16px;font-style:italic;margin-bottom:8px}
  .reasons__list{list-style:none}
  .reasons__item{display:flex;gap:8px;font-size:7px;line-height:1.4;margin-bottom:9px}
  .reasons__num{flex:none;width:11px;height:11px;border-radius:50%;background:var(--red);color:#fff;font-size:7px;font-weight:700;display:flex;align-items:center;justify-content:center}

  /* inside right */
  .grid{display:grid;grid-template-columns:1fr 1fr;grid-template-rows:repeat(3,1fr);height:100%}
  .cell{position:relative}
  .cell--photo-office{background:linear-gradient(150deg,#f2f2f2 0%,#d8dcd8 60%,#4e9a54 100%)}
  .cell--photo-surface{background:linear-gradient(150deg,#f4f0ea 0%,#d6ccbf 55%,#e7cf3a 100%)}
  .cell--photo-supplies{background:linear-gradient(150deg,#e9e6e1 0%,#cfcac3 50%,#2e6fcf 85%,#d8382f 100%)}
  .cell--info{background:var(--blue-deep);color:#fff;border-top:6px solid var(--red);padding:20px 14px 10px 18px}
  .info-list{list-style:none}
  .info-list li{position:relative;padding-left:12px;font-size:6.8px;line-height:1.4;margin-bottom:12px}
  .info-list li::before{content:"";position:absolute;left:0;top:2px;width:5px;height:5px;border-radius:50%;background:#fff}
</style>
</head>
<body>

<section class="spread spread--outside">
  <article class="page back">
    <div class="photo back__photo" role="img" aria-label="Photo area: cleaner in blue apron holding a green mop and a bucket of cleaning supplies"></div>
    <div class="brand back__brand"><span class="brand__dot"></span><span>Brightmoor Cleaning Services</span></div>
    <div class="contact">
      <div class="contact__row">
        <svg width="9" height="11" viewBox="0 0 9 11"><path d="M4.5 0A4 4 0 0 0 .5 4c0 3 4 7 4 7s4-4 4-7a4 4 0 0 0-4-4z" fill="#1a6dbf"/><circle cx="4.5" cy="4" r="1.5" fill="#fff"/></svg>
        <span>472 Kestrel Ridge W Ste 518<br>Tukwila, WA 98102</span>
      </div>
      <div class="contact__row">
        <svg width="10" height="10" viewBox="0 0 10 10"><circle cx="5" cy="5" r="4.3" fill="none" stroke="#1a6dbf" stroke-width="1"/><path d="M3.4 3c.3 1.6 1.8 3.2 3.4 3.6l.4-.7-.9-.5-.5.4c-.6-.3-1.1-.8-1.4-1.4l.4-.5-.5-.9z" fill="#1a6dbf"/></svg>
        <span class="contact__phone">877-514-SHINE</span>
      </div>
      <div class="contact__row">
        <svg width="10" height="10" viewBox="0 0 10 10"><circle cx="5" cy="5" r="4.3" fill="none" stroke="#1a6dbf"/><ellipse cx="5" cy="5" rx="2" ry="4.3" fill="none" stroke="#1a6dbf" stroke-width=".8"/><line x1=".7" y1="5" x2="9.3" y2="5" stroke="#1a6dbf" stroke-width=".8"/></svg>
        <span>www.brightmoorclean.com</span>
      </div>
    </div>
  </article>

  <article class="page front">
    <header class="front__band">
      <h1 class="front__headline">The most through carpet<br>cleaning ever ... or it's free !</h1>
    </header>
    <div class="photo front__photo" role="img" aria-label="Photo area: bright living room being vacuumed"></div>
    <aside class="testimonials">
      <h2 class="testimonials__title">
        <svg width="14" height="11" viewBox="0 0 14 11"><circle cx="5" cy="3" r="2.3" fill="#fff"/><path d="M0.5 11c0-3 2-4.5 4.5-4.5S9.5 8 9.5 11z" fill="#fff"/><circle cx="10" cy="3.5" r="1.8" fill="#fff"/><path d="M10 6.5c2 0 3.5 1.3 3.5 4H10.5" fill="#fff"/></svg>
        TESTIMONIALS
      </h2>
      <div class="review">
        <p class="review__head">Lorem ipsum dolor sit amet !</p>
        <p class="review__by">by Lorem Ipsum</p>
        <p class="review__stars">★★★★★</p>
        <p class="review__text">Lorem ipsum dolor sit amet, consectetur adipiscing elit, sed do eiusmod tempor incididunt ut labore et dolore magna aliqua. Ut enim ad minim veniam, quis nostrud exercitation ullamco laboris nisi ut aliquip ex ea commodo consequat.</p>
      </div>
      <div class="review">
        <p class="review__head">Lorem ipsum dolor sit amet !</p>
        <p class="review__by">by Lorem Ipsum</p>
        <p class="review__stars">★★★★★</p>
        <p class="review__text">Lorem ipsum dolor sit amet, consectetur adipiscing elit, sed do eiusmod tempor incididunt ut labore et dolore magna aliqua. Ut enim ad minim veniam, quis nostrud exercitation ullamco laboris nisi ut aliquip ex ea commodo consequat.</p>
      </div>
    </aside>
    <p class="front__url">www.brightmoorclean.com</p>
    <div class="brand front__brand"><span class="brand__dot"></span><span>Brightmoor Cleaning Services</span></div>
  </article>
</section>

<section class="spread spread--inside">
  <article class="page inside-left">
    <h2 class="words__title">You have my words</h2>
    <p class="body-text">Lorem ipsum dolor sit amet, consectetur adipiscing elit, sed do eiusmod tempor incididunt ut labore et dolore magna aliqua. Ut enim ad minim veniam, quis nostrud exercitation ullamco laboris nisi ut aliquip ex ea commodo consequat. Lorem ipsum dolor sit amet, consectetur adipiscing elit, sed do eiusmod tempor incididunt ut labore et dolore magna aliqua. Ut enim ad minim veniam, quis nostrud exercitation ullamco laboris nisi ut aliquip ex ea commodo consequat.</p>

    <div class="quote-block">
      <blockquote class="quote-box">
        <span class="quote-box__mark quote-box__mark--open">“</span>
        Lorem ipsum dolor sit amet, consectetur adipiscing elit, sed do eiusmod tempor incididunt ut labore et dolore magna aliqua. Ut enim ad minim veniam, quis nostrud exercitation ullamco laboris nisi ut aliquip ex ea commodo consequat. Lorem ipsum dolor sit amet, consectetur adipiscing elit, sed do eiusmod tempor incididunt ut labore et dolore magna aliqua. Ut enim ad minim veniam, quis nostrud exercitation ullamco laboris nisi ut aliquip ex ea commodo consequat.
        <p class="quote-box__by">- Lorem Ipsum</p>
        <span class="quote-box__mark quote-box__mark--close">”</span>
      </blockquote>
      <div class="quote-photo" role="img" aria-label="Round photo area: kitchen surface being wiped clean"></div>
    </div>

    <div class="carpet">
      <h3 class="section-title">Ready to give up on your Carpet ?</h3>
      <p class="body-text">Lorem ipsum dolor sit amet, consectetur adipiscing elit, sed do eiusmod tempor incididunt ut labore et dolore magna aliqua. Ut enim ad minim veniam, quis nostrud exercitation ullamco laboris nisi ut aliquip ex ea commodo consequat. Lorem ipsum dolor sit amet, consectetur adipiscing elit, sed do eiusmod tempor incididunt ut labore et dolore magna aliqua. Ut enim ad minim veniam, quis nostrud exercitation ullamco laboris nisi ut aliquip ex ea commodo consequat.</p>
    </div>

    <div class="reasons">
      <h3 class="section-title">Reasons why you'll love my company</h3>
      <ol class="reasons__list">
        <li class="reasons__item"><span class="reasons__num">1</span><span>Lorem ipsum dolor sit amet, consectetur adipiscing elit, sed do eiusmod tempor incididunt ut labore et dolore magna aliqua. Ut enim ad minim veniam, quis nostrud exercitation ullamco laboris nisi ut aliquip ex ea commodo consequat.</span></li>
        <li class="reasons__item"><span class="reasons__num">2</span><span>Lorem ipsum dolor sit amet, consectetur adipiscing elit, sed do eiusmod tempor incididunt ut labore et dolore magna aliqua. Ut enim ad minim veniam, quis nostrud exercitation ullamco laboris nisi ut aliquip ex ea commodo consequat.</span></li>
        <li class="reasons__item"><span class="reasons__num">3</span><span>Lorem ipsum dolor sit amet, consectetur adipiscing elit, sed do eiusmod tempor incididunt ut labore et dolore magna aliqua. Ut enim ad minim veniam, quis nostrud exercitation ullamco.</span></li>
        <li class="reasons__item"><span class="reasons__num">4</span><span>Lorem ipsum dolor sit amet, consectetur adipiscing elit, sed do eiusmod tempor incididunt ut labore et dolore magna aliqua. Ut enim ad minim veniam, quis nostrud exercitation ullamco.</span></li>
      </ol>
    </div>
  </article>

  <article class="page inside-right">
    <div class="grid">
      <div class="cell cell--photo-office" role="img" aria-label="Photo area: office being cleaned, green accents"></div>
      <div class="cell cell--info">
        <ul class="info-list">
          <li>Lorem ipsum dolor sit amet, consectetur adipiscing elit.</li>
          <li>Lorem ipsum dolor sit amet, consectetur adipiscing elit, sed do eiusmod tempor</li>
          <li>Lorem ipsum dolor sit amet, consectetur adipiscing elit, sed do eiusmod tempor incididunt ut labore et dolore magna aliqua.</li>
        </ul>
      </div>
      <div class="cell cell--info">
        <ul class="info-list">
          <li>Lorem ipsum dolor sit amet, consectetur adipiscing elit.</li>
          <li>Lorem ipsum dolor sit amet, consectetur adipiscing elit, sed do eiusmod tempor incididunt ut labore et dolore magna aliqua.</li>
          <li>Lorem ipsum dolor sit amet, consectetur adipiscing elit, sed do eiusmod tempor</li>
        </ul>
      </div>
      <div class="cell cell--photo-surface" role="img" aria-label="Photo area: table surface wiped with yellow glove and spray bottle"></div>
      <div class="cell cell--photo-supplies" role="img" aria-label="Photo area: bucket of cleaning supplies on a floor"></div>
      <div class="cell cell--info">
        <ul class="info-list">
          <li>Lorem ipsum dolor sit amet, consectetur adipiscing elit.</li>
          <li>Lorem ipsum dolor sit amet, consectetur adipiscing elit, sed do eiusmod tempor incididunt ut labore et dolore magna aliqua.</li>
          <li>Lorem ipsum dolor sit amet, consectetur adipiscing elit, sed do eiusmod tempor</li>
        </ul>
      </div>
    </div>
  </article>
</section>

</body>
</html>
```